Letterhead Design Needed for Real Estate Office

We are a boutique real estate agency focused on property management. We need a letter head which is professional looking and include the following information:

Logo
ABN Number
Address
Postal Address
Phone
Fax
Mobile
Email
Website

Please note that the PLVAQT logo can not be changed and must be positioned at the bottom right corner.

Please find attached the existing letterhead design for all the required elements.

Target Market(s)

Letterhead mostly used for service of notices, business letters, clients communication

Industry/Entity Type

Boutique

Colors

Designer to choose colors to be used in the design.

Requirements
Must have
• Logo

```html
<!DOCTYPE html>
<html lang="en">
<head>
<meta charset="utf-8">
<title>Meridian Partners Letterhead</title>
<link rel="stylesheet" href="https://fonts.googleapis.com/css2?family=Ubuntu:wght@400;500;700&display=swap">
<style>
  :root {
    --brand-green: #a5c73a;
    --brand-green-light: #bcd561;
    --brand-green-pale: #cfe0a0;
    --ink: #1d1d1b;
    --brand-dark: #4a4a48;
    --partner-navy: #1d3f8a;
    --paper: #ffffff;
  }
  html, body {
    margin: 0;
    padding: 0;
    overflow: hidden;
    background: var(--paper);
  }
  .letterhead {
    position: relative;
    width: 848px;
    height: 1200px;
    overflow: hidden;
    background: var(--paper);
    font-family: "Ubuntu", sans-serif;
    color: var(--ink);
  }
  .brand {
    position: absolute;
    left: 44px;
    top: 50px;
    display: flex;
    align-items: center;
    gap: 14px;
  }
  .brand-square {
    width: 44px;
    height: 44px;
    background: var(--brand-green);
  }
  .brand-name {
    font-size: 30px;
    font-weight: 700;
    color: var(--brand-dark);
    letter-spacing: 0.5px;
  }
  .contact {
    position: absolute;
    left: 340px;
    top: 22px;
    width: 484px;
    text-align: center;
    font-size: 14px;
    line-height: 19px;
  }
  .contact p { margin: 0; }
  .contact b { font-weight: 700; }
  .band {
    position: absolute;
    left: 0;
    background: var(--brand-green);
  }
  .band-top-thick { top: 134px; width: 848px; height: 9px; }
  .band-top-thin { top: 151px; width: 848px; height: 5px; background: var(--brand-green-light); }
  .band-foot-thick { top: 1137px; width: 610px; height: 7px; }
  .band-foot-thin { top: 1154px; width: 610px; height: 6px; background: var(--brand-green-light); }
  .corner-mark {
    position: absolute;
    left: 40px;
    top: 1000px;
    width: 96px;
    height: 96px;
    background: var(--brand-green-pale);
  }
  .partner {
    position: absolute;
    left: 640px;
    top: 1092px;
    display: flex;
    align-items: center;
    gap: 10px;
  }
  .partner-square {
    width: 30px;
    height: 30px;
    background: var(--partner-navy);
  }
  .partner-name {
    font-size: 30px;
    font-weight: 700;
    color: var(--partner-navy);
  }
</style>
</head>
<body>
<main class="letterhead">
  <header>
    <div class="brand">
      <span class="brand-square"></span>
      <span class="brand-name">Meridian Partners</span>
    </div>
    <address class="contact" style="font-style:normal">
      <p>ABN 48 302 615 729</p>
      <p>Shop 12B 210-224 Wattle Street Lindfield NSW 2070 AUSTRALIA</p>
      <p>PO BOX 415 Lindfield NSW 2070</p>
      <p><b>m</b> 0400 555 172 | <b>p</b> 9555 0142</p>
      <p><b>f</b> 9555 0143 | <b>e</b> info@mprealty.cc | <b>w</b> http://mprealty.cc</p>
    </address>
  </header>
  <div class="band band-top-thick"></div>
  <div class="band band-top-thin"></div>

  <footer>
    <div class="corner-mark" aria-hidden="true"></div>
    <div class="band band-foot-thick"></div>
    <div class="band band-foot-thin"></div>
    <div class="partner">
      <span class="partner-square"></span>
      <span class="partner-name">PLVAQT</span>
    </div>
  </footer>
</main>
</body>
</html>
```